Broschüre für Baumanagement
Zielgruppe
Baumanagement
Wir liefern von der Planung, über die notwendigen Handwerksfirmen langjährige Partner, Bauleitung alle notwenidgen Partner
Wir betreuen seit jahren Kunden aus dem Immobilienwesen, Handel usw.
Ein Ansprechpartner vond er Planung bis zur Übergabe
Aufgabenstellung
DIN A4, 2 Seiten, Modern, Fakten, Gerne nur in schwarz und weiss halten

```html
<!DOCTYPE html>
<html lang="de">
<head>
<meta charset="utf-8">
<title>Baumanagement Broschüre</title>
<link href="https://fonts.googleapis.com/css2?family=Montserrat:wght@500;600;700;800&display=swap" rel="stylesheet">
<style>
  :root {
    --stage: #b9b9b9;
    --paper: #ffffff;
    --ink: #0d0d0d;
    --grey-light: #e4e4e4;
    --photo-dark: #363636;
    --photo-mid: #7b7b7b;
    --photo-light: #cfcfcf;
    --sky: #d9dadc;
    --glass-mid: #8c8f94;
    --glass-dark: #2e3033;
  }
  * { margin: 0; padding: 0; box-sizing: border-box; }
  html, body {
    width: 906px; height: 1200px; overflow: hidden;
    background: linear-gradient(180deg, #c4c4c4, var(--stage));
    font-family: "Montserrat", sans-serif;
  }
  .spread {
    position: absolute; left: 13px; top: 294px;
    width: 1397px; height: 970px;
    transform: scale(0.63); transform-origin: 0 0;
  }
  .page {
    position: absolute; top: 0; width: 687px; height: 970px;
    background: var(--paper); overflow: hidden;
    box-shadow: 0 10px 30px rgba(0,0,0,.35);
  }
  .page--back { left: 0; }
  .page--front { left: 710px; }
  .page svg.bg { position: absolute; inset: 0; width: 687px; height: 970px; }

  .brand {
    position: absolute; display: flex; align-items: center; gap: 12px;
    color: var(--ink); font-weight: 800; white-space: nowrap;
  }
  .brand__mark { background: var(--ink); display: inline-block; }

  .back__title { position: absolute; left: 74px; top: 46px; color: var(--paper); font-size: 26px; font-weight: 700; }
  .back__body { position: absolute; left: 74px; top: 86px; color: var(--paper); font-size: 19.5px; font-weight: 500; line-height: 24.5px; }
  .back__lead { position: absolute; left: 74px; top: 168px; color: var(--paper); font-size: 18.5px; font-weight: 700; line-height: 25px; }
  .back__brand { left: 345px; top: 350px; font-size: 22px; }
  .back__brand .brand__mark { width: 26px; height: 26px; }

  .contact { position: absolute; left: 74px; top: 790px; color: var(--ink); }
  .contact__label { font-size: 24px; font-weight: 700; }
  .contact__phone { display: flex; align-items: center; gap: 10px; font-size: 50px; font-weight: 800; line-height: 62px; }
  .contact__phone svg { width: 36px; height: 36px; }
  .contact__web { font-size: 24px; font-weight: 500; letter-spacing: 6.5px; }

  .front__brand { left: 0; right: 0; top: 92px; justify-content: center; font-size: 36px; }
  .front__brand .brand__mark { width: 40px; height: 40px; }
  .front__claim {
    position: absolute; left: 400px; top: 183px;
    font-size: 22px; font-weight: 600; line-height: 27.5px; text-transform: uppercase; color: var(--ink);
  }
  .front__claim strong { font-weight: 800; }
</style>
</head>
<body>
<main class="spread">

  <section class="page page--back">
    <svg class="bg" viewBox="0 0 687 970">
      <defs>
        <linearGradient id="deskPhoto" x1="0" y1="0" x2="1" y2="1">
          <stop offset="0" stop-color="var(--photo-light)"/>
          <stop offset="0.5" stop-color="var(--photo-mid)"/>
          <stop offset="1" stop-color="var(--photo-dark)"/>
        </linearGradient>
      </defs>
      <rect x="0" y="200" width="687" height="770" fill="url(#deskPhoto)" role="img" aria-label="Foto: Hände unterzeichnen einen Vertrag neben einem Hausmodell auf dem Schreibtisch"/>
      <polygon points="0,0 687,0 687,215 272,360 0,460" fill="var(--ink)"/>
      <polygon points="272,360 687,215 687,440" fill="var(--paper)"/>
      <polygon points="0,620 687,870 687,970 0,970" fill="var(--paper)"/>
      <polygon points="0,620 150,675 0,760" fill="var(--grey-light)"/>
    </svg>
    <h2 class="back__title">Baumanagement</h2>
    <p class="back__body">Wir liefern von der Planung, über die notwendigen<br>Handwerksfirmen langjährige Partner, Bauleitung<br>alle notwenidgen Partner</p>
    <p class="back__lead">Ein Ansprechpartner vond er Planung<br>bis zur Übergabe</p>
    <div class="brand back__brand"><span class="brand__mark"></span>STEINWERK GROUP</div>
    <div class="contact">
      <p class="contact__label">Kontaktieren Sie uns</p>
      <p class="contact__phone">
        <svg viewBox="0 0 36 36" aria-hidden="true"><circle cx="18" cy="18" r="17" fill="var(--ink)"/><path d="M12 10c1-1 2-1 3 0l2 3c.5 1 .3 1.7-.5 2.4l-1 .8c1 2.3 2.7 4 5 5l.8-1c.7-.8 1.4-1 2.4-.5l3 2c1 1 1 2 0 3l-1.5 1.5c-1.5 1.2-4 .8-7.5-1.8s-6.5-6.5-7-9.5c-.3-1.5.1-2.7 1.3-3.9z" fill="var(--paper)"/></svg>
        123-456-7890
      </p>
      <p class="contact__web">www.website.com</p>
    </div>
  </section>

  <section class="page page--front">
    <svg class="bg" viewBox="0 0 687 970">
      <defs>
        <linearGradient id="towerPhoto" x1="0.3" y1="0" x2="0.6" y2="1">
          <stop offset="0" stop-color="var(--sky)"/>
          <stop offset="0.45" stop-color="var(--glass-mid)"/>
          <stop offset="1" stop-color="var(--glass-dark)"/>
        </linearGradient>
        <linearGradient id="sideTowers" x1="0" y1="0" x2="1" y2="1">
          <stop offset="0" stop-color="#c9c9c9"/>
          <stop offset="1" stop-color="#4a4a4a"/>
        </linearGradient>
      </defs>
      <g role="img" aria-label="Foto: Glashochhäuser von unten gegen den Himmel">
        <polygon class="photo-side" points="0,214 67,240 67,970 0,970" fill="url(#sideTowers)"/>
        <polygon class="photo-main" points="67,272 358,184 362,184 362,970 67,970" fill="url(#towerPhoto)"/>
        <polygon class="photo-side" points="366,350 687,450 687,970 366,970" fill="url(#sideTowers)"/>
        <polygon class="photo-inner" points="395,482 597,555 597,970 395,970" fill="url(#towerPhoto)"/>
        <polygon class="photo-inner" points="0,510 122,550 122,918 0,880" fill="#5b5b5b"/>
      </g>
      <polygon points="560,395 687,365 687,450" fill="var(--grey-light)"/>
      <g class="frame-strips" fill="none" stroke="var(--paper)" stroke-width="8" stroke-linejoin="miter">
        <polyline points="358,184 67,272 67,516 164,554 164,974"/>
        <line x1="364" y1="184" x2="364" y2="974"/>
        <polyline points="395,974 395,482 597,555 597,974"/>
        <polyline points="-4,510 122,550 122,918 -4,880"/>
      </g>
    </svg>
    <div class="brand front__brand"><span class="brand__mark"></span>STEINWERK GROUP</div>
    <p class="front__claim">We advise and<br>mediate<br>primarily in the<br>commercial and<br><strong>residential<br>asset classes.</strong></p>
  </section>

</main>
</body>
</html>
```